A Health & Fitness Website selling saunas and Cold tubs

www.tarnwellgear.com, www.frostvaleco, www.brimholdsupply
Design a website
We are selling saunas, infrared saunas, cold plunge tubs, and massage chairs to financially successful MEN.
We want professional, simple, masculine with a touch of sexy.
One section for each… saunas, cold plunge tubs, massage chairs.
Each will have at least two buy links to their affiliate/supplier/store.
The landing page / opening page / needs big & bold; a full screen image? a great picture showing the warmth of a sauna? Need your ideas
The pictures are everything.

The Website for our book
https://maplewickvigor.com/

Coding

Coded - Design and coding required

Number of Pages Required

1 page

Requirements
Must have
• Great pictures

```html
<!DOCTYPE html>
<html lang="en">
<head>
<meta charset="utf-8">
<title>Maplewick Vigor — Saunas, Cold Plunge Tubs &amp; Massage Chairs</title>
<link href="https://fonts.googleapis.com/css2?family=Poppins:wght@400;500;600;700;800&display=swap" rel="stylesheet">
<style>
:root{
  --orange:#ee6a1f;
  --orange-deep:#e8461e;
  --ink:#1c1c1c;
  --muted:#444;
  --grey-panel:#f1f1f1;
  --white:#fff;
  --line:#dcdcdc;
  --star:#f5b400;
}
*{box-sizing:border-box;margin:0;padding:0}
html,body{width:1200px;height:3553px;overflow:hidden}
body{font-family:'Poppins',sans-serif;color:var(--ink);background:var(--white);position:relative}
.abs{position:absolute}
.btn{display:flex;align-items:center;justify-content:center;gap:12px;background:linear-gradient(90deg,var(--orange),var(--orange-deep));color:#fff;font-weight:600;font-size:15px;border-radius:30px;text-transform:uppercase;letter-spacing:.2px}
.btn svg{width:18px;height:18px}
.accent{color:var(--orange);font-weight:700}

/* header */
.tagline{left:86px;top:36px;font-size:16px;line-height:20px;font-weight:500}
.phone{left:733px;top:36px;display:flex;gap:14px;align-items:center}
.phone-icon{width:36px;height:36px;border-radius:50%;background:var(--orange);display:flex;align-items:center;justify-content:center}
.phone small{display:block;font-size:15px;color:var(--muted)}
.phone strong{font-size:19px;font-weight:600}
.header-btn{left:978px;top:38px;width:136px;height:39px}

/* hero */
.hero{left:0;top:113px;width:1200px;height:662px;background:linear-gradient(100deg,#7a2f14 0%,#9a4a22 35%,#c37a44 60%,#a65e33 100%)}
.hero-title{left:86px;top:250px;font-size:48px;font-weight:700;line-height:54px;color:#fff}
.hero-title span{color:var(--orange)}
.hero-sub{left:86px;top:436px;width:520px;font-size:17px;line-height:24px;color:#fff}
.store-btn{left:86px;top:517px;width:184px;height:59px;border-radius:30px;background:#111;border:2px solid #fff;color:#fff;text-align:center;padding-top:6px}
.store-btn small{display:block;font-size:11px}
.store-btn b{font-size:22px;font-weight:600}
.hero-curve{left:0;top:620px}

.logo-badge{left:481px;top:0;width:238px;height:238px;border-radius:50%;background:#fff;display:flex;align-items:center;justify-content:center;text-align:center;font-weight:700;font-size:22px;line-height:26px;color:var(--ink)}

/* circulation */
.center{left:0;width:1200px;text-align:center}
.circ-title{top:755px;font-size:42px}
.circ-sub{top:818px;font-size:21px;font-weight:600}
.circ-btn{left:532px;top:870px;width:136px;height:38px}

/* benefits */
.benefits{left:86px;top:965px;width:1028px;height:555px;background:var(--grey-panel);border-radius:40px}
.benefits h2{position:absolute;top:40px;width:100%;text-align:center;font-size:40px;font-weight:400}
.benefits h2 b{color:var(--orange)}
.benefits .lead{position:absolute;top:100px;width:100%;text-align:center;font-size:21px;font-weight:600}
.list{position:absolute;top:160px;width:412px}
.list li{list-style:none;height:36px;border-bottom:1px solid var(--line);display:flex;align-items:center;gap:24px;font-size:17px;padding-left:6px}
.list li svg{width:20px;height:20px;flex:none}
.benefits .close{position:absolute;top:487px;width:100%;text-align:center;font-size:34px}

/* products */
.section-title{font-size:42px}
.prod-title{top:1572px}
.card{border-radius:30px;overflow:hidden}
.card .label{position:absolute;left:40px;bottom:40px;color:#fff;font-size:28px;font-weight:700}
.sauna{left:86px;top:1659px;width:505px;height:556px;background:linear-gradient(120deg,#4a2e18,#9a6a3d 45%,#5b7b86)}
.plunge{left:609px;top:1659px;width:505px;height:269px;background:linear-gradient(160deg,#5f8a3f,#3a4a3a 60%,#222)}
.chair{left:609px;top:1946px;width:505px;height:269px;background:linear-gradient(120deg,#a12a2a,#3a4c88 55%,#7a1c22)}
.sauna-btn{position:absolute;right:40px;bottom:35px;width:136px;height:38px}

/* testimonials */
.test-title{top:2262px}
.tcard{width:289px;border-radius:12px;background:#fff;box-shadow:0 4px 18px rgba(0,0,0,.1);text-align:center;padding:34px 22px 0;font-size:11.5px;line-height:19.5px;color:#333}
.tcard.featured{background:linear-gradient(160deg,var(--orange),var(--orange-deep));color:#fff}
.stars{display:flex;gap:4px;justify-content:center;margin-bottom:18px}
.stars svg{width:21px;height:21px}
.row1{top:2353px;height:280px}
.row2{top:2649px;height:279px}
.c1{left:130px}.c2{left:456px}.c3{left:781px}
.load-btn{left:529px;top:2975px;width:147px;height:38px}

/* newsletter */
.divider{left:0;top:3063px;width:1200px;height:1px;background:var(--line)}
.news-title{top:3088px;font-size:40px;font-weight:800}
.news-title span{color:var(--orange-deep)}
.news-sub{top:3143px;font-size:15px}
.news-form{left:364px;top:3192px;width:467px;height:44px;display:flex}
.news-form .field{flex:1;background:#ececec;border-radius:22px 0 0 22px;display:flex;align-items:center;padding-left:28px;font-size:14px}
.news-form .send{width:128px;background:linear-gradient(90deg,var(--orange-deep),var(--orange));border-radius:0 22px 22px 0;color:#fff;font-size:14px;font-weight:600;display:flex;align-items:center;justify-content:center}
.foot-logo{left:516px;top:3255px;width:168px;height:168px;border-radius:50%;border:3px solid var(--ink);display:flex;align-items:center;justify-content:center;text-align:center;font-weight:700;font-size:18px;line-height:22px}
.socials{left:525px;top:3470px;display:flex;gap:26px}
.socials span{width:19px;height:19px;border-radius:50%;background:#8a8a8a;display:block}
.copy{top:3512px;font-size:14px}
</style>
</head>
<body>

<!-- Header -->
<div class="abs tagline">Top of the Line Health Products<br>Exclusively for the Financially Successful</div>
<div class="abs phone">
  <div class="phone-icon"><svg width="18" height="18" viewBox="0 0 24 24" fill="#fff"><path d="M6.6 10.8a15.2 15.2 0 006.6 6.6l2.2-2.2c.3-.3.7-.4 1-.2 1.1.4 2.3.6 3.6.6.6 0 1 .4 1 1V20c0 .6-.4 1-1 1A17 17 0 013 4c0-.6.4-1 1-1h3.5c.6 0 1 .4 1 1 0 1.3.2 2.5.6 3.6.1.3 0 .7-.2 1z"/></svg></div>
  <div><small>Call Us Today</small><strong>(800) 555-0147</strong></div>
</div>
<div class="abs btn header-btn">Buy Now <svg viewBox="0 0 20 20"><circle cx="10" cy="10" r="9" fill="#fff"/><path d="M6 10h7M10 6.5l3.5 3.5L10 13.5" stroke="var(--orange)" stroke-width="2" fill="none"/></svg></div>

<!-- Hero -->
<div class="abs hero" role="img" aria-label="Couple relaxing together in a warm wooden sauna"></div>
<h1 class="abs hero-title"><span>Dramatically</span><br>Improve Your Health<br>Without Exercise</h1>
<p class="abs hero-sub">Successful Men Recognize the Importance of Their Health and Make it a Priority. It’s Your Time. You’ve Earned it.</p>
<div class="abs store-btn"><small>Order now at</small><b>Northmart</b></div>
<svg class="abs hero-curve" width="1200" height="160" viewBox="0 0 1200 160">
  <defs><linearGradient id="arc" x1="0" x2="1"><stop offset="0" stop-color="#ee6a1f"/><stop offset="1" stop-color="#e8461e"/></linearGradient></defs>
  <path d="M0 150 Q600 -100 1200 150 L1200 160 L0 160Z" fill="url(#arc)"/>
  <path d="M0 160 Q600 -60 1200 160Z" fill="#fff"/>
</svg>
<div class="abs logo-badge">MAPLEWICK<br>VIGOR</div>

<!-- Circulation -->
<h2 class="abs center circ-title" style="font-weight:400">A Mans Body Thrives on <span class="accent">Circulation</span></h2>
<p class="abs center circ-sub">And It Doesn’t Care How You Get It.</p>
<div class="abs btn circ-btn">Buy Now <svg viewBox="0 0 20 20"><circle cx="10" cy="10" r="9" fill="#fff"/><path d="M6 10h7M10 6.5l3.5 3.5L10 13.5" stroke="var(--orange)" stroke-width="2" fill="none"/></svg></div>

<!-- Benefits -->
<section class="abs benefits">
  <h2>WHEN THERE’S NO TIME FOR <b>EXERCISE</b>.</h2>
  <p class="lead">Use Hot, Cold, or Massage. The Benefits are Numerous.</p>
  <ul class="list" style="left:76px">
    <li><svg viewBox="0 0 20 20"><path d="M3 10l5 5L17 4" stroke="#e8461e" stroke-width="3" fill="none"/></svg>RELIEVE STRESS</li>
    <li><svg viewBox="0 0 20 20"><path d="M3 10l5 5L17 4" stroke="#e8461e" stroke-width="3" fill="none"/></svg>DETOX YOUR PORES</li>
    <li><svg viewBox="0 0 20 20"><path d="M3 10l5 5L17 4" stroke="#e8461e" stroke-width="3" fill="none"/></svg>SLEEP BETTER</li>
    <li><svg viewBox="0 0 20 20"><path d="M3 10l5 5L17 4" stroke="#e8461e" stroke-width="3" fill="none"/></svg>RELIEVE MUSCLE TENSION</li>
    <li><svg viewBox="0 0 20 20"><path d="M3 10l5 5L17 4" stroke="#e8461e" stroke-width="3" fill="none"/></svg>BOOST ENERGY LEVELS</li>
    <li><svg viewBox="0 0 20 20"><path d="M3 10l5 5L17 4" stroke="#e8461e" stroke-width="3" fill="none"/></svg>INCREASE TESTOSTERONE</li>
    <li><svg viewBox="0 0 20 20"><path d="M3 10l5 5L17 4" stroke="#e8461e" stroke-width="3" fill="none"/></svg>REDUCE INFLAMMATION</li>
    <li><svg viewBox="0 0 20 20"><path d="M3 10l5 5L17 4" stroke="#e8461e" stroke-width="3" fill="none"/></svg>INCREASE IMMUNITY REDUCE</li>
  </ul>
  <ul class="list" style="left:542px">
    <li><svg viewBox="0 0 20 20"><path d="M3 10l5 5L17 4" stroke="#e8461e" stroke-width="3" fill="none"/></svg>DEPRESSION</li>
    <li><svg viewBox="0 0 20 20"><path d="M3 10l5 5L17 4" stroke="#e8461e" stroke-width="3" fill="none"/></svg>ALLEVIATE JOINT PAIN</li>
    <li><svg viewBox="0 0 20 20"><path d="M3 10l5 5L17 4" stroke="#e8461e" stroke-width="3" fill="none"/></svg>HEALTHIER SKIN</li>
    <li><svg viewBox="0 0 20 20"><path d="M3 10l5 5L17 4" stroke="#e8461e" stroke-width="3" fill="none"/></svg>LOWER THE RISK OF CARDIOVASCULAR</li>
    <li><svg viewBox="0 0 20 20"><path d="M3 10l5 5L17 4" stroke="#e8461e" stroke-width="3" fill="none"/></svg>DISEASE</li>
    <li><svg viewBox="0 0 20 20"><path d="M3 10l5 5L17 4" stroke="#e8461e" stroke-width="3" fill="none"/></svg>INCREASE METABOLISM</li>
    <li><svg viewBox="0 0 20 20"><path d="M3 10l5 5L17 4" stroke="#e8461e" stroke-width="3" fill="none"/></svg>PROMOTE WEIGHT LOSS</li>
    <li><svg viewBox="0 0 20 20"><path d="M3 10l5 5L17 4" stroke="#e8461e" stroke-width="3" fill="none"/></svg>A LONGER &amp; HEALTHIER LIFE</li>
  </ul>
  <p class="close"><b>Specific Improvements</b> will be Individual to You.</p>
</section>

<!-- Products -->
<h2 class="abs center section-title prod-title" style="font-weight:400">Our <span class="accent">Products</span></h2>
<div class="abs card sauna" role="img" aria-label="Woman relaxing in a sunlit wooden sauna">
  <span class="label">All Saunas</span>
  <div class="btn sauna-btn">Buy Now <svg viewBox="0 0 20 20"><circle cx="10" cy="10" r="9" fill="#fff"/><path d="M6 10h7M10 6.5l3.5 3.5L10 13.5" stroke="var(--orange)" stroke-width="2" fill="none"/></svg></div>
</div>
<div class="abs card plunge" role="img" aria-label="Woman in an outdoor cold plunge tub surrounded by trees"><span class="label">Cold Plunge Tubs</span></div>
<div class="abs card chair" role="img" aria-label="Woman resting in a red massage chair"><span class="label">Massage Chairs</span></div>

<!-- Testimonials -->
<h2 class="abs center section-title test-title" style="font-weight:400">Clients <span class="accent">Testimonials</span></h2>

<div class="abs tcard row1 c1"><div class="stars"><svg viewBox="0 0 24 24"><path fill="var(--star)" d="M12 2l3 7 7 .6-5.4 4.7L18.2 22 12 18l-6.2 4 1.6-7.7L2 9.6 9 9z"/></svg><svg viewBox="0 0 24 24"><path fill="var(--star)" d="M12 2l3 7 7 .6-5.4 4.7L18.2 22 12 18l-6.2 4 1.6-7.7L2 9.6 9 9z"/></svg><svg viewBox="0 0 24 24"><path fill="var(--star)" d="M12 2l3 7 7 .6-5.4 4.7L18.2 22 12 18l-6.2 4 1.6-7.7L2 9.6 9 9z"/></svg><svg viewBox="0 0 24 24"><path fill="var(--star)" d="M12 2l3 7 7 .6-5.4 4.7L18.2 22 12 18l-6.2 4 1.6-7.7L2 9.6 9 9z"/></svg><svg viewBox="0 0 24 24"><path fill="var(--star)" d="M12 2l3 7 7 .6-5.4 4.7L18.2 22 12 18l-6.2 4 1.6-7.7L2 9.6 9 9z"/></svg></div>I climb in my sauna half asleep every morning for 20 minutes before I take a shower and head off to work. It’s the only thing I found that really wakes me up in the morning. I’m not a coffee drinker so that’s never been an option but this sauna is the perfect morning wake up</div>

<div class="abs tcard featured row1 c2"><div class="stars"><svg viewBox="0 0 24 24"><path fill="var(--star)" d="M12 2l3 7 7 .6-5.4 4.7L18.2 22 12 18l-6.2 4 1.6-7.7L2 9.6 9 9z"/></svg><svg viewBox="0 0 24 24"><path fill="var(--star)" d="M12 2l3 7 7 .6-5.4 4.7L18.2 22 12 18l-6.2 4 1.6-7.7L2 9.6 9 9z"/></svg><svg viewBox="0 0 24 24"><path fill="var(--star)" d="M12 2l3 7 7 .6-5.4 4.7L18.2 22 12 18l-6.2 4 1.6-7.7L2 9.6 9 9z"/></svg><svg viewBox="0 0 24 24"><path fill="var(--star)" d="M12 2l3 7 7 .6-5.4 4.7L18.2 22 12 18l-6.2 4 1.6-7.7L2 9.6 9 9z"/></svg><svg viewBox="0 0 24 24"><path fill="var(--star)" d="M12 2l3 7 7 .6-5.4 4.7L18.2 22 12 18l-6.2 4 1.6-7.7L2 9.6 9 9z"/></svg></div>I had no idea how much inflammation I had in my body. It wasn’t until the relief I got from my cold plunge that I realized how bad joints were. It’s been a life changing relief.</div>

<div class="abs tcard row1 c3"><div class="stars"><svg viewBox="0 0 24 24"><path fill="var(--star)" d="M12 2l3 7 7 .6-5.4 4.7L18.2 22 12 18l-6.2 4 1.6-7.7L2 9.6 9 9z"/></svg><svg viewBox="0 0 24 24"><path fill="var(--star)" d="M12 2l3 7 7 .6-5.4 4.7L18.2 22 12 18l-6.2 4 1.6-7.7L2 9.6 9 9z"/></svg><svg viewBox="0 0 24 24"><path fill="var(--star)" d="M12 2l3 7 7 .6-5.4 4.7L18.2 22 12 18l-6.2 4 1.6-7.7L2 9.6 9 9z"/></svg><svg viewBox="0 0 24 24"><path fill="var(--star)" d="M12 2l3 7 7 .6-5.4 4.7L18.2 22 12 18l-6.2 4 1.6-7.7L2 9.6 9 9z"/></svg><svg viewBox="0 0 24 24"><path fill="var(--star)" d="M12 2l3 7 7 .6-5.4 4.7L18.2 22 12 18l-6.2 4 1.6-7.7L2 9.6 9 9z"/></svg></div>I love a good massage but making an appointment is almost impossible with my schedule. The chair is always there. I climb in and let it do its thing. I forget about work so much that it usually turns in to a power nap.</div>

<div class="abs tcard row2 c1"><div class="stars"><svg viewBox="0 0 24 24"><path fill="var(--star)" d="M12 2l3 7 7 .6-5.4 4.7L18.2 22 12 18l-6.2 4 1.6-7.7L2 9.6 9 9z"/></svg><svg viewBox="0 0 24 24"><path fill="var(--star)" d="M12 2l3 7 7 .6-5.4 4.7L18.2 22 12 18l-6.2 4 1.6-7.7L2 9.6 9 9z"/></svg><svg viewBox="0 0 24 24"><path fill="var(--star)" d="M12 2l3 7 7 .6-5.4 4.7L18.2 22 12 18l-6.2 4 1.6-7.7L2 9.6 9 9z"/></svg><svg viewBox="0 0 24 24"><path fill="var(--star)" d="M12 2l3 7 7 .6-5.4 4.7L18.2 22 12 18l-6.2 4 1.6-7.7L2 9.6 9 9z"/></svg><svg viewBox="0 0 24 24"><path fill="var(--star)" d="M12 2l3 7 7 .6-5.4 4.7L18.2 22 12 18l-6.2 4 1.6-7.7L2 9.6 9 9z"/></svg></div>I’ve always loved a good sweat. It just feels so rejuvenating. I guess I relate it to when I was younger and got a good sweat through exercise. A nice shower to rinse it all away and I feel like a new person. To finally have a sauna at my home is simply the best. No more finding time to go to the gym, I could jump into my sauna anytime I want.</div>

<div class="abs tcard row2 c2"><div class="stars"><svg viewBox="0 0 24 24"><path fill="var(--star)" d="M12 2l3 7 7 .6-5.4 4.7L18.2 22 12 18l-6.2 4 1.6-7.7L2 9.6 9 9z"/></svg><svg viewBox="0 0 24 24"><path fill="var(--star)" d="M12 2l3 7 7 .6-5.4 4.7L18.2 22 12 18l-6.2 4 1.6-7.7L2 9.6 9 9z"/></svg><svg viewBox="0 0 24 24"><path fill="var(--star)" d="M12 2l3 7 7 .6-5.4 4.7L18.2 22 12 18l-6.2 4 1.6-7.7L2 9.6 9 9z"/></svg><svg viewBox="0 0 24 24"><path fill="var(--star)" d="M12 2l3 7 7 .6-5.4 4.7L18.2 22 12 18l-6.2 4 1.6-7.7L2 9.6 9 9z"/></svg><svg viewBox="0 0 24 24"><path fill="var(--star)" d="M12 2l3 7 7 .6-5.4 4.7L18.2 22 12 18l-6.2 4 1.6-7.7L2 9.6 9 9z"/></svg></div>We’re your typical old married couple. After 24 years we don’t have time together very often. I had been using my cold plunge for about two months pretty religiously every weekend and I knew the changes it made in me. I had not felt that energetic in years. One lively night we both stayed up late and talked for hours. Of course it hasn’t fixed everything but it feels good to be energized again.</div>

<div class="abs tcard row2 c3"><div class="stars"><svg viewBox="0 0 24 24"><path fill="var(--star)" d="M12 2l3 7 7 .6-5.4 4.7L18.2 22 12 18l-6.2 4 1.6-7.7L2 9.6 9 9z"/></svg><svg viewBox="0 0 24 24"><path fill="var(--star)" d="M12 2l3 7 7 .6-5.4 4.7L18.2 22 12 18l-6.2 4 1.6-7.7L2 9.6 9 9z"/></svg><svg viewBox="0 0 24 24"><path fill="var(--star)" d="M12 2l3 7 7 .6-5.4 4.7L18.2 22 12 18l-6.2 4 1.6-7.7L2 9.6 9 9z"/></svg><svg viewBox="0 0 24 24"><path fill="var(--star)" d="M12 2l3 7 7 .6-5.4 4.7L18.2 22 12 18l-6.2 4 1.6-7.7L2 9.6 9 9z"/></svg><svg viewBox="0 0 24 24"><path fill="var(--star)" d="M12 2l3 7 7 .6-5.4 4.7L18.2 22 12 18l-6.2 4 1.6-7.7L2 9.6 9 9z"/></svg></div>I hate exercise. I love my work. If I’m not working I’m relaxing and thinking about work. 24/7 I’m on. I have the dual plunge, hot and cold. I use the cold more in the summer, it’s incredibly refreshing. I use the hot more in the winter. I occasionally do both but usually I only have time for one. When I’m refreshed, I’m more productive. When I’m productive I make more money. That’s what I’m all about.</div>

<div class="abs btn load-btn">Load More <svg viewBox="0 0 20 20"><circle cx="10" cy="10" r="9" fill="#fff"/><path d="M6 10h7M10 6.5l3.5 3.5L10 13.5" stroke="var(--orange)" stroke-width="2" fill="none"/></svg></div>

<!-- Newsletter & footer -->
<div class="abs divider"></div>
<h2 class="abs center news-title">Subscribe to <span>Newsletter</span></h2>
<p class="abs center news-sub">Enter your email address to register to our newsletter subscription!</p>
<div class="abs news-form"><div class="field">Email address</div><div class="send">SEND NOW</div></div>
<div class="abs foot-logo">MAPLEWICK<br>VIGOR</div>
<div class="abs socials"><span></span><span></span><span></span><span></span></div>
<p class="abs center copy">Copyright © 2024 Maplewick Vigor I All Right Reserved</p>

</body>
</html>
```